Design for a 4 screens mobile app: Brelluvo

The app is a compact but illustrated phone/address book...
We need a design for the 5 screens of the app (see screens attached):
a) "index" : 1 screen with 6 pictures of contact person
b) "contact list" : 1 screen, to manage (add/del/edit) the contacts of the phone/address book
c) "add contact" : 1 screen to add a contact (a picture + a phone number)
d) "update contact" : similar to "add"
e) "fields missing" : add/edit screens in "error" state
We also need the ico design + loading screen.
No specific guidelines, nor logo or whatever.
It will be a free app distributed on iOS and Androïd.
We just want to make it looking nice & very usable for end users.
B2C

```html
<!DOCTYPE html>
<html lang="en">
<head>
<meta charset="UTF-8">
<title>Brelluvo – Add contact</title>
<link href="https://fonts.googleapis.com/css2?family=Open+Sans:wght@400;600&display=swap" rel="stylesheet">
<style>
  :root {
    --brand-pink: #e91e63;
    --surface: #ffffff;
    --on-brand: #ffffff;
    --icon-ink: #3a3a3a;
  }
  * { box-sizing: border-box; margin: 0; padding: 0; }
  html, body {
    width: 800px;
    height: 1200px;
    overflow: hidden;
    background: var(--surface);
    font-family: "Open Sans", Arial, sans-serif;
  }
  .add-screen {
    position: relative;
    width: 800px;
    height: 1200px;
    background: var(--surface);
  }
  .app-bar {
    position: absolute;
    top: 0; left: 0;
    width: 100%;
    height: 135px;
    background: var(--brand-pink);
    color: var(--on-brand);
  }
  .app-bar__back {
    position: absolute;
    left: 34px;
    top: 72px;
    width: 36px;
    height: 30px;
  }
  .app-bar__title {
    position: absolute;
    left: 0; right: 0;
    top: 66px;
    text-align: center;
    font-size: 34px;
    font-weight: 400;
    letter-spacing: 1px;
    line-height: 1;
  }
  .app-bar__save {
    position: absolute;
    right: 37px;
    top: 74px;
    font-size: 25px;
    font-weight: 400;
    letter-spacing: 1.5px;
    line-height: 1;
  }
  .photo-picker {
    position: absolute;
    left: 282px;
    top: 448px;
    width: 236px;
    height: 144px;
  }
  .phone-field {
    position: absolute;
    left: 75px;
    top: 916px;
    width: 650px;
    height: 99px;
    border: 2px solid var(--brand-pink);
    border-radius: 4px;
  }
  .phone-field__caret {
    position: absolute;
    left: 50%;
    top: 24px;
    width: 2px;
    height: 49px;
    margin-left: -1px;
    background: var(--brand-pink);
  }
  .gallery-button {
    position: absolute;
    left: 710px;
    top: 1126px;
    width: 50px;
    height: 46px;
  }
</style>
</head>
<body>
  <main class="add-screen">
    <header class="app-bar">
      <svg class="app-bar__back" viewBox="0 0 36 30" aria-label="Back">
        <path d="M34 15 H4 M16 3 L4 15 L16 27" fill="none" stroke="currentColor" stroke-width="3" stroke-linecap="round" stroke-linejoin="round"/>
      </svg>
      <h1 class="app-bar__title">ADD</h1>
      <span class="app-bar__save">SAVE</span>
    </header>

    <svg class="photo-picker" viewBox="0 0 173 125" aria-label="Add a photo">
      <rect x="25" y="0" width="40" height="22" rx="7" fill="var(--brand-pink)"/>
      <rect x="0" y="13" width="173" height="112" rx="14" fill="var(--brand-pink)"/>
      <circle cx="101" cy="70" r="31" fill="none" stroke="var(--surface)" stroke-width="10"/>
      <circle cx="152" cy="34" r="8" fill="var(--surface)"/>
    </svg>

    <div class="phone-field" aria-label="Phone number">
      <span class="phone-field__caret"></span>
    </div>

    <svg class="gallery-button" viewBox="0 0 50 46" aria-label="Choose from gallery">
      <g fill="none" stroke="var(--icon-ink)" stroke-width="2.2" stroke-linejoin="round">
        <rect x="3" y="5" width="38" height="30" rx="3" transform="rotate(-6 22 20)"/>
        <rect x="8" y="11" width="38" height="31" rx="3" fill="var(--surface)"/>
        <polyline points="11,38 21,27 28,33 34,27 43,38"/>
        <circle cx="37" cy="19" r="3"/>
      </g>
    </svg>
  </main>
</body>
</html>
```